Hautglanz Kosmetik Göttingen sucht Werbeplakat für Außenwerbung
Zielgruppe
Wir sind ein junges modernes Kosmetikstudio im Herzen der Studentenstadt Göttingen.
Wir bieten allen Zielgruppen ein attraktives Preisleistungsverhältnis.
http://www.hautglanz-kosmetik.example/
Aufgabenstellung
Wir benötigen für ein großes Außenplakat eine ansprechende Werbung für unser Studio.
Schwerpunkt sollte dabei unser Angebot für dauerhafte Haarentfernung mittels IPL Technologie sein.
Es soll optisch ansprechend sein (eye catcher) und auch Studenten ansprechen.

```html
<!DOCTYPE html>
<html lang="de">
<head>
<meta charset="utf-8">
<title>Hautglanz Kosmetik – Dauerhafte Haarenfernung</title>
<link href="https://fonts.googleapis.com/css2?family=Tinos:wght@400;700&display=swap" rel="stylesheet">
<style>
  :root {
    --violet-deep: #5a2a8c;
    --violet: #8a4cc4;
    --violet-mid: #a873dc;
    --lilac: #cfa9f0;
    --lilac-pale: #eedcfb;
    --white: #ffffff;
    --ink: #3c1a5e;
    --skin: #d9a27c;
  }
  * { margin: 0; padding: 0; box-sizing: border-box; }
  html, body { width: 848px; height: 1200px; overflow: hidden; background: var(--white); }
  .poster {
    position: relative;
    width: 848px;
    height: 1200px;
    overflow: hidden;
    font-family: "Tinos", "Times New Roman", serif;
    color: var(--ink);
    background:
      radial-gradient(circle at 560px 160px, rgba(255,255,255,0.85) 0, rgba(255,255,255,0) 180px),
      radial-gradient(circle at 780px 420px, rgba(255,255,255,0.35) 0, rgba(255,255,255,0) 90px),
      radial-gradient(circle at 470px 640px, rgba(255,255,255,0.3) 0, rgba(255,255,255,0) 80px),
      radial-gradient(circle at 120px 900px, rgba(255,255,255,0.9) 0, rgba(255,255,255,0) 260px),
      linear-gradient(160deg, var(--violet-mid) 0%, var(--lilac) 45%, var(--violet-mid) 75%, var(--violet) 100%);
  }
  .hero-photo {
    position: absolute;
    left: 0; top: 0;
    width: 420px; height: 1085px;
    background:
      linear-gradient(180deg, rgba(160,100,210,0.9) 0%, rgba(190,140,230,0.8) 28%, rgba(217,162,124,0.75) 34%, rgba(217,162,124,0.7) 78%, rgba(160,100,210,0.85) 88%, rgba(255,255,255,0) 100%);
    clip-path: polygon(0 0, 100% 0, 78% 30%, 62% 100%, 15% 100%, 0 30%);
  }
  .bottom-band { position: absolute; left: 0; top: 1060px; width: 848px; height: 140px; }
  .headline-top {
    position: absolute; left: 560px; top: 38px;
    font-size: 44px; font-weight: 700; color: var(--violet-deep);
    text-shadow: 0 0 6px var(--white), 0 0 2px var(--white);
  }
  .headline-main {
    position: absolute; left: 135px; top: 100px;
    font-size: 102px; font-weight: 700; color: var(--white);
    -webkit-text-stroke: 3px var(--violet-deep);
    paint-order: stroke fill;
    transform: rotate(-4deg); transform-origin: left center;
    text-shadow: 3px 4px 6px rgba(60,26,94,0.5);
    letter-spacing: 0.5px;
  }
  .offer-box {
    position: absolute; left: 416px; top: 272px;
    width: 404px; height: 600px;
    background: rgba(238,220,251,0.55);
    border: 2px solid rgba(255,255,255,0.85);
    box-shadow: 0 0 12px rgba(90,42,140,0.25);
    text-align: center;
  }
  .offer-title {
    margin-top: 40px;
    font-size: 31px; font-weight: 700; line-height: 57px; color: var(--ink);
  }
  .offer-list { list-style: none; margin-top: 62px; font-size: 21px; line-height: 26px; color: var(--ink); }
  .offer-list li { margin: 0 24px 18px; }
  .brand-card {
    position: absolute; left: 355px; top: 860px;
    width: 470px; height: 170px;
    background: var(--white);
    transform: rotate(-10deg);
    box-shadow: 2px 4px 10px rgba(60,26,94,0.35);
    text-align: center;
    padding-top: 18px;
  }
  .brand-name { font-size: 62px; font-weight: 700; color: var(--violet-deep); line-height: 70px; }
  .brand-tagline { font-size: 30px; color: var(--violet-deep); line-height: 38px; }
  .brand-services { font-size: 15px; color: var(--ink); margin-top: 8px; }
  .contact { position: absolute; left: 0; width: 848px; text-align: center; color: var(--white); }
  .contact-phone { top: 1112px; font-size: 40px; }
  .contact-address { top: 1163px; font-size: 21px; }
</style>
</head>
<body>
<main class="poster">
  <div class="hero-photo" role="img" aria-label="Foto: Beine einer Frau in lila Kleid und lila Sandaletten mit Absatz"></div>

  <svg class="bottom-band" viewBox="0 0 848 140" width="848" height="140" aria-hidden="true">
    <defs>
      <linearGradient id="bandFill" x1="0" y1="0" x2="1" y2="0">
        <stop offset="0" stop-color="#6b3399"/>
        <stop offset="0.5" stop-color="#8a4cc4"/>
        <stop offset="1" stop-color="#6b3399"/>
      </linearGradient>
    </defs>
    <path d="M0 40 Q424 0 848 30 L848 140 L0 140 Z" fill="url(#bandFill)"/>
    <path d="M0 40 Q424 0 848 30" fill="none" stroke="#ffffff" stroke-width="3" opacity="0.8"/>
  </svg>

  <h1>
    <span class="headline-top">Dauerhafte</span>
    <span class="headline-main">Haarenfernung</span>
  </h1>

  <section class="offer-box">
    <h2 class="offer-title">Immer perfekt<br>zu jedem Anlass</h2>
    <ul class="offer-list">
      <li>Kostenlose Beratung</li>
      <li>Neueste IPL Technologie aus Deutschland</li>
      <li>Besonders schonend für Ihre Haut</li>
      <li>Für alle Körperpartien geeignet</li>
      <li>Nie wieder rasieren, epillieren oder wachsen!</li>
    </ul>
  </section>

  <div class="brand-card">
    <div class="brand-name">Hautglanz</div>
    <div class="brand-tagline">Dein Kosmetikstudio in Göttingen</div>
    <div class="brand-services">Dauerhafte Haarentfernung • Kosmetik • Naildesign • Fußpflege</div>
  </div>

  <p class="contact contact-phone">Tel: 0551-12 34 56 78</p>
  <p class="contact contact-address">Lindenallee 14 - 37073 Göttingen</p>
</main>
</body>
</html>
```